Palm Cove Villas - Rental Villa Website

I have a villa for rent in Thailand and require a website - i need to demo pictures/walk through video, local attractions, villa facilities description plus seaonal rates and online booking.

Industry/Entity Type

Rental

Coding

Coded - Design and coding required

```html
<!DOCTYPE html>
<html lang="en">
<head>
<meta charset="utf-8">
<title>Palm Cove Villas – Villa Rental</title>
<link href="https://fonts.googleapis.com/css2?family=Roboto:ital,wght@0,300;0,400;0,500;0,700;1,300;1,400&family=Open+Sans:wght@400;600&display=swap" rel="stylesheet">
<style>
:root{
  --plum:#4e2f3b;
  --plum-dark:#3d2430;
  --page:#f2f0f1;
  --ink:#2b2b2b;
  --muted:#6a6a6a;
  --line:#dcdcdc;
  --white:#ffffff;
  --footer:#191919;
  --footer-panel:#232323;
  --footer-strip:#2a2a2a;
  --field-dark:#141414;
}
*{box-sizing:border-box;margin:0;padding:0}
html,body{width:1200px;height:2830px;overflow:hidden}
body{position:relative;background:var(--page);font-family:"Open Sans",Arial,sans-serif;color:var(--ink)}
.abs{position:absolute}
.heading{font-family:"Roboto",Arial,sans-serif}

/* top bar */
.topbar{left:0;top:0;width:1200px;height:42px;background:var(--plum);color:var(--white);font-size:12px}
.topbar .address{left:143px;top:13px;display:flex;align-items:center;gap:7px}
.social{display:flex;gap:8px}
.social span{width:26px;height:26px;background:var(--white);border-radius:2px;display:block}
.topbar .social{left:552px;top:8px}
.topbar .book{left:986px;top:8px;width:78px;height:27px;background:var(--white);color:var(--ink);font-size:11px;font-weight:600;display:flex;align-items:center;justify-content:center;border-radius:2px}

/* header */
.header{left:0;top:42px;width:1200px;height:107px;background:var(--white)}
.brand{display:flex;align-items:center;gap:10px;font-family:"Roboto",Arial,sans-serif;font-weight:400;color:var(--plum-dark);white-space:nowrap}
.brand .dot{width:14px;height:14px;border-radius:50%;background:currentColor}
.header .brand{left:124px;top:36px;font-size:30px}
.nav{right:118px;top:46px;display:flex;gap:42px;font-size:12px;color:#444}

/* hero */
.hero{left:0;top:149px;width:1200px;height:552px;background:linear-gradient(100deg,#3b2e28 0%,#8a7a6a 30%,#d9d6d0 50%,#b8c8a0 72%,#6c7460 85%,#9aa0a8 100%)}
.slide-arrow{width:38px;height:38px;background:var(--white);border-radius:3px;display:flex;align-items:center;justify-content:center}
.hero .prev{left:29px;top:258px}
.hero .next{left:1131px;top:258px}

/* reservation */
.reserve{left:180px;top:617px;width:840px;height:331px;background:linear-gradient(180deg,rgba(196,212,210,.95),rgba(160,186,184,.95) 60%,rgba(190,200,196,.95));}
.reserve-shadow{left:220px;top:940px;width:760px;height:40px;border-radius:50%;background:radial-gradient(ellipse at center,rgba(0,0,0,.55),rgba(0,0,0,0) 70%)}
.reserve h2{position:absolute;left:0;right:0;top:30px;text-align:center;font-family:"Roboto",Arial,sans-serif;font-weight:400;font-size:30px;color:#222}
.reserve .lead{position:absolute;left:0;right:0;top:76px;text-align:center;font-size:13px;color:#333}
.field{position:absolute;top:147px}
.field label{display:block;font-size:11px;font-weight:600;color:#222;margin-bottom:9px}
.field .box{height:36px;background:var(--white);border:1px solid #cfcfcf;font-size:10px;color:#999;display:flex;align-items:center;justify-content:space-between;padding:0 9px}
.reserve .submit{position:absolute;left:351px;top:245px;width:136px;height:34px;background:var(--plum);color:var(--white);font-size:13px;font-weight:600;display:flex;align-items:center;justify-content:center;border-radius:3px}

/* section titles */
.section-title{left:0;width:1200px;text-align:center;font-family:"Roboto",Arial,sans-serif}
.section-title h2{font-size:34px;font-weight:300;font-style:italic}
.section-title h2 b{font-weight:500}
.section-title p{font-size:12px;font-style:italic;margin-top:2px}
.section-title i.rule{display:block;width:62px;height:8px;margin:6px auto 0;border:1px solid currentColor;border-top:none}

/* deals */
.deal-photo{left:124px;top:1116px;width:463px;height:355px;background:linear-gradient(100deg,#3c302a,#8a7d70 35%,#d4d0cb 55%,#b0b4b8 80%,#7d858c)}
.deal-arrow{top:1222px}
.deal-title{left:612px;top:1110px;font-size:22px;font-weight:400}
.deal-meta{left:612px;top:1166px;display:flex;gap:22px;font-size:11px;color:#333}
.deal-meta span{display:flex;align-items:center;gap:6px}
.deal-text{left:612px;top:1200px;width:464px;font-size:12px;line-height:17px;color:#666;text-align:justify}
.features{left:516px;top:1295px;width:382px;height:150px;background:var(--white);border:1px solid #e2e2e2;box-shadow:0 2px 8px rgba(0,0,0,.08);padding:15px 25px 0 18px}
.features li{list-style:none;display:flex;align-items:center;gap:14px;height:40px;font-size:12px;color:#555;background:#f6f6f6;padding-left:10px;margin-bottom:4px}
.price{left:927px;top:1295px;width:149px;height:150px;background:var(--white);border:1px solid #e2e2e2;text-align:center;padding-top:30px}
.price .per{font-size:15px;color:#555}
.price .amount{font-size:34px;font-family:"Roboto",Arial,sans-serif;font-weight:300;color:var(--plum)}
.price .book-now{margin:8px auto 0;width:84px;height:28px;background:var(--plum);color:var(--white);font-size:10px;display:flex;align-items:center;justify-content:center}

/* retreat */
.retreat{left:0;top:1515px;width:1200px;height:405px;background:linear-gradient(100deg,#6c6862,#8d8a82 30%,#5b5048 55%,#6e7a6a 80%,#45503e)}
.retreat-title{top:1552px;color:var(--white)}
.card{top:1649px;width:300px;height:352px;background:var(--white);padding:17px 16px 20px}
.card .photo{position:relative;width:100%;height:100%;border-radius:3px;color:var(--white);text-align:center;padding:92px 18px 0;overflow:hidden}
.card h3{font-family:"Roboto",Arial,sans-serif;font-weight:400;font-size:32px;line-height:36px}
.card h4{font-family:"Roboto",Arial,sans-serif;font-weight:400;font-size:20px;line-height:24px;margin-top:2px}
.card p{font-size:11px;line-height:15px;margin-top:12px}
.card-shadow{top:1998px;width:280px;height:24px;border-radius:50%;background:radial-gradient(ellipse at center,rgba(0,0,0,.6),rgba(0,0,0,0) 70%)}

/* map */
.map{left:0;top:2052px;width:1200px;height:350px;background:linear-gradient(90deg,#bcd6ea 0%,#d8e2c8 20%,#e4e4d4 50%,#dfe3cd 75%,#bcd6ea 100%)}

/* footer */
.footer{left:0;top:2402px;width:1200px;height:283px;background:var(--footer)}
.footer .brand{position:absolute;left:124px;top:76px;font-size:26px;color:var(--white)}
.footer .about{position:absolute;left:124px;top:124px;width:220px;font-size:11px;line-height:16px;color:#ddd;text-align:justify}
.contact{left:369px;top:2324px;width:462px;height:361px;background:var(--footer-panel);color:var(--white);text-align:center;border-radius:3px 3px 0 0;z-index:2}
.contact h2{font-family:"Roboto",Arial,sans-serif;font-weight:400;font-size:26px;margin-top:36px}
.contact .sub{font-size:12px;margin-top:2px}
.contact .input{position:absolute;left:82px;width:298px;background:var(--field-dark);border:1px solid #333;font-size:10px;color:#777;text-align:left;padding:12px 14px}
.contact .send{position:absolute;left:174px;top:342px;width:113px;height:32px;background:var(--white);color:var(--ink);font-size:10px;font-weight:600;display:flex;align-items:center;justify-content:center;border-radius:2px}
.gallery-title{left:858px;top:2464px;font-family:"Roboto",Arial,sans-serif;font-size:28px;font-weight:400;color:var(--white)}
.thumb{width:66px;height:66px}
.strip{left:0;top:2685px;width:1200px;height:76px;background:var(--footer-strip);color:var(--white);font-size:12px;z-index:1}
.strip .item{position:absolute;top:31px;display:flex;align-items:center;gap:9px}
.strip .social{position:absolute;left:976px;top:26px}
.strip .social span{background:none;border:1px solid var(--white)}
.copyright{left:0;top:2761px;width:1200px;height:69px;background:var(--footer);color:#ddd;font-size:11px;text-align:center;line-height:69px}
</style>
</head>
<body>

<div class="abs topbar">
  <div class="abs address">
    <svg width="10" height="13" viewBox="0 0 10 13"><path d="M5 0a5 5 0 0 0-5 5c0 3.5 5 8 5 8s5-4.5 5-8a5 5 0 0 0-5-5zm0 7a2 2 0 1 1 0-4 2 2 0 0 1 0 4z" fill="#fff"/></svg>
    1234 Street Name, City Name, United States
  </div>
  <div class="abs social"><span></span><span></span><span></span></div>
  <div class="abs book">BOOK</div>
</div>

<header class="abs header">
  <div class="abs brand"><i class="dot"></i>Palm Cove Villas</div>
  <nav class="abs nav"><span>Home</span><span>About Us</span><span>Gallery</span><span>Blog</span><span>Contact Us</span></nav>
</header>

<section class="abs hero" role="img" aria-label="Villa bedroom interior with wooden furniture, wall art and a view to the garden">
  <div class="abs slide-arrow prev"><svg width="10" height="14" viewBox="0 0 10 14"><path d="M8 1 2 7l6 6" fill="none" stroke="#333" stroke-width="2"/></svg></div>
  <div class="abs slide-arrow next"><svg width="10" height="14" viewBox="0 0 10 14"><path d="m2 1 6 6-6 6" fill="none" stroke="#333" stroke-width="2"/></svg></div>
</section>

<div class="abs reserve-shadow"></div>
<form class="abs reserve" role="img" aria-label="Villa pool photograph behind the reservation form">
  <h2>Villa Reservation</h2>
  <p class="lead">We're in the business of exceeding expect ations. We give you exactly</p>
  <div class="field" style="left:25px;width:177px"><label>ARRIVAL</label><div class="box">Select Date<svg width="12" height="12" viewBox="0 0 12 12"><rect x="1" y="2" width="10" height="9" fill="none" stroke="#999"/><path d="M1 5h10M4 1v2M8 1v2" stroke="#999"/></svg></div></div>
  <div class="field" style="left:229px;width:178px"><label>DEPARTURE</label><div class="box">Select Date<svg width="12" height="12" viewBox="0 0 12 12"><rect x="1" y="2" width="10" height="9" fill="none" stroke="#999"/><path d="M1 5h10M4 1v2M8 1v2" stroke="#999"/></svg></div></div>
  <div class="field" style="left:433px;width:111px"><label>ADULTS</label><div class="box">1<svg width="8" height="12" viewBox="0 0 8 12"><path d="M1 5 4 2l3 3M1 7l3 3 3-3" fill="none" stroke="#777"/></svg></div></div>
  <div class="field" style="left:571px;width:109px"><label>KIDS</label><div class="box">1<svg width="8" height="12" viewBox="0 0 8 12"><path d="M1 5 4 2l3 3M1 7l3 3 3-3" fill="none" stroke="#777"/></svg></div></div>
  <div class="field" style="left:707px;width:107px"><label>ROOMS</label><div class="box">1<svg width="8" height="12" viewBox="0 0 8 12"><path d="M1 5 4 2l3 3M1 7l3 3 3-3" fill="none" stroke="#777"/></svg></div></div>
  <div class="submit">SUBMIT NOW</div>
</form>

<div class="abs section-title" style="top:1015px;color:#222">
  <h2><b>Villa</b> Latest Deals</h2>
  <p>Aenean commodo ligula egt tash piscing elit enean</p>
  <i class="rule"></i>
</div>

<svg class="abs deal-arrow" style="left:32px" width="30" height="54" viewBox="0 0 30 54"><path d="M28 1 2 27l26 26" fill="none" stroke="#999" stroke-width="1.5"/></svg>
<svg class="abs deal-arrow" style="left:1138px" width="30" height="54" viewBox="0 0 30 54"><path d="m2 1 26 26L2 53" fill="none" stroke="#999" stroke-width="1.5"/></svg>

<div class="abs deal-photo" role="img" aria-label="Villa bedroom with bed, armchair and wall painting"></div>
<h3 class="abs deal-title heading">Free High Speed Wi-Fi Internet in Room</h3>
<div class="abs deal-meta">
  <span><svg width="9" height="12" viewBox="0 0 10 13"><path d="M5 0a5 5 0 0 0-5 5c0 3.5 5 8 5 8s5-4.5 5-8a5 5 0 0 0-5-5zm0 7a2 2 0 1 1 0-4 2 2 0 0 1 0 4z" fill="#333"/></svg>1234 Street Name, City Name, United States</span>
  <span><svg width="12" height="12" viewBox="0 0 12 12"><path d="M11 1 1 5l4 1 1 4 2-3 3 2z" fill="#333"/></svg>Sky Air</span>
  <span><svg width="14" height="11" viewBox="0 0 14 11"><path d="M2 5 3.5 1h7L12 5h1v4h-2v2H9V9H5v2H3V9H1V5z" fill="#333"/></svg>Free Transport</span>
</div>
<p class="abs deal-text">Duis at ante nec neque rhoncus pretium. Ut placerat euismod nibh industry's stand orci donec mollis, est non scelerisque blandit, velit nunc laoreet dol scrambled it to augue non elit aliquam in vehicula sem phasellu consectetur adipiscing elit donec porttitor lectus at neque sollicitudin.</p>

<ul class="abs features">
  <li><svg width="16" height="12" viewBox="0 0 16 12"><path d="M1 4a10 10 0 0 1 14 0M3.5 6.5a6.5 6.5 0 0 1 9 0M6 9a3 3 0 0 1 4 0" fill="none" stroke="#666" stroke-width="1.4"/><circle cx="8" cy="11" r="1" fill="#666"/></svg>Free High Speed Wi-Fi Internet in Room</li>
  <li><svg width="16" height="12" viewBox="0 0 14 11"><path d="M2 5 3.5 1h7L12 5h1v4h-2v2H9V9H5v2H3V9H1V5z" fill="#666"/></svg>Free Private Parking is Available</li>
  <li><svg width="16" height="16" viewBox="0 0 16 16"><path d="M4 1v5M2 1v4a2 2 0 0 0 4 0V1M4 7v8M11 1c-2 1-2 6 0 7v7" fill="none" stroke="#666" stroke-width="1.4"/></svg>In Room Dining is Available 09:00 P.M. - 12:09 P.M.</li>
</ul>
<div class="abs price">
  <div class="per">PER DAY</div>
  <div class="amount">$ 45</div>
  <div class="book-now">BOOK NOW</div>
</div>

<section class="abs retreat" role="img" aria-label="Terrace overlooking a green valley and lake"></section>
<div class="abs section-title retreat-title">
  <h2><b>LUXURIOUS</b> RETREAT</h2>
  <p>Aenean commodo ligula egt tash piscing elit enean</p>
  <i class="rule"></i>
</div>

<div class="abs card-shadow" style="left:134px"></div>
<div class="abs card-shadow" style="left:460px"></div>
<div class="abs card-shadow" style="left:784px"></div>

<article class="abs card" style="left:124px">
  <div class="photo" role="img" aria-label="Villa room interior" style="background:linear-gradient(160deg,#5c564e,#2f2a26 60%,#433b34)">
    <h3>Special Room</h3><h4>Rooms &amp; Facilities</h4>
    <p>ipsum dolor sit amet, consectetur dipisicing elit. Magi aliqua ut enim ad erat lorem ipsum gentia elit.</p>
  </div>
</article>
<article class="abs card" style="left:451px">
  <div class="photo" role="img" aria-label="Villa rooftop and garden" style="background:linear-gradient(160deg,#6e5a48,#4a3c30 50%,#3c4a34)">
    <h3>Function</h3><h4>Rooms &amp; Facilities</h4>
    <p>ipsum dolor sit amet, consectetur dipisicing elit. Magi aliqua ut enim ad erat lorem ipsum gentia elit.</p>
  </div>
</article>
<article class="abs card" style="left:774px">
  <div class="photo" role="img" aria-label="Swimming pool by the lake" style="background:linear-gradient(180deg,#9aa4a4,#5e7470 40%,#2f5a50)">
    <h3>Swiming Pull</h3><h4>Clean And Sharp</h4>
    <p>ipsum dolor sit amet, consectetur dipisicing elit. Magi aliqua ut enim ad erat lorem ipsum gentia elit.</p>
  </div>
</article>

<section class="abs map" role="img" aria-label="Road map of Thailand and neighbouring countries showing the villa region"></section>

<footer class="abs footer">
  <div class="brand"><i class="dot"></i>Palm Cove Villas</div>
  <p class="about">Ut wisi enim ad minim veniam, quis nostrud tation ullamcorper suscipit loborts nisl ut ali ea commodo consequat. Lorem ipsum doloi et, consectetuer adipiscng elitre.</p>
</footer>

<h3 class="abs gallery-title">Gallery</h3>
<div class="abs thumb" style="left:858px;top:2512px;background:linear-gradient(160deg,#9fb4b4,#4d7a78)" role="img" aria-label="Pool view"></div>
<div class="abs thumb" style="left:932px;top:2512px;background:linear-gradient(160deg,#7a6a5a,#cfc8be)" role="img" aria-label="Bedroom"></div>
<div class="abs thumb" style="left:1006px;top:2512px;background:linear-gradient(160deg,#8c9a9a,#3f6a66)" role="img" aria-label="Terrace by the pool"></div>
<div class="abs thumb" style="left:858px;top:2590px;background:linear-gradient(160deg,#5a626a,#bcc0c2)" role="img" aria-label="Living room"></div>
<div class="abs thumb" style="left:932px;top:2590px;background:linear-gradient(160deg,#6a5040,#3a4a32)" role="img" aria-label="Villa roof and garden"></div>
<div class="abs thumb" style="left:1006px;top:2590px;background:linear-gradient(160deg,#b8c4c0,#6a9a94)" role="img" aria-label="Pool deck"></div>

<div class="abs strip">
  <div class="item" style="left:124px"><svg width="13" height="13" viewBox="0 0 13 13"><circle cx="6.5" cy="6.5" r="6" fill="#fff"/><path d="M1 6.5h11M6.5 .5c-3 3-3 9 0 12M6.5 .5c3 3 3 9 0 12" fill="none" stroke="#2a2a2a"/></svg>stay@palmcovevillas.com</div>
  <div class="item" style="left:396px"><svg width="13" height="13" viewBox="0 0 13 13"><path d="M3 1 5 4 4 5.5c1 2 2 3 3.5 3.5L9 8l3 2-1 2C6 12 1 7 1 2z" fill="#fff"/></svg>+12 5550143877</div>
  <div class="social"><span></span><span></span><span></span></div>
</div>

<section class="abs contact">
  <h2>CONTACT US</h2>
  <p class="sub">Aenean commodo ligula egt tash piscing</p>
  <div class="input" style="top:112px;height:44px">Enter Your Name</div>
  <div class="input" style="top:166px;height:45px">Enter Your Email</div>
  <div class="input" style="top:223px;height:101px">Message</div>
  <div class="send">SUBMIT NOW</div>
</section>

<div class="abs copyright">© Copyright 2015 &nbsp; | &nbsp; Palm Cove Villas &nbsp; | &nbsp; All Rights Reserved</div>

</body>
</html>
```